Road Construction Company needs business cards

We would like a new business card designed for our business.

We're a road construction company based in Qld, Australia.

Can the business card please have the following information on it.

Name: Brent Malvoy
Position: General Manager
Phone: 0471 592 304
Email: Brent.malvoy@quendix.com.au
Address: 87 Harrowgate Ave, Pindarra, QLD, 4000
Website: www.quendix.com.au

Visually we'd like the card to be professional and simple.

Attached is our logo.

Our website is www.quendix.com.au

Target Market(s)

Men aged 25-60

Contact Information for Business Card

As listed in project description

Font styles to use
Serif

Requirements
Must have
• Large logo on back of card

```html
<!DOCTYPE html>
<html lang="en">
<head>
<meta charset="utf-8">
<title>Quendix Business Card</title>
<link href="https://fonts.googleapis.com/css2?family=Open+Sans:wght@400;600;700&display=swap" rel="stylesheet">
<style>
  :root {
    --stage: #6e6e70;
    --card: #211f1f;
    --card-deep: #1a1818;
    --pattern-light: #2b2929;
    --blue: #1f5fb8;
    --blue-line: #2a6fb5;
    --text: #e6e6e6;
  }
  * { margin: 0; padding: 0; box-sizing: border-box; }
  html, body {
    width: 1200px; height: 900px; overflow: hidden;
    background: var(--stage);
    font-family: "Open Sans", Arial, sans-serif;
  }
  .stage {
    position: relative; width: 1200px; height: 900px;
  }
  .card {
    position: absolute; left: 285px; width: 630px; height: 360px;
    background: var(--card); overflow: hidden;
    box-shadow: 0 10px 28px rgba(0,0,0,.35);
  }
  .card-back { top: 60px; border-radius: 26px; }
  .card-front { top: 480px; border-radius: 6px 60px 6px 60px; }

  .back-pattern {
    position: absolute; inset: 0;
    background: linear-gradient(135deg, var(--pattern-light) 0%, var(--card) 50%, var(--card-deep) 100%);
  }
  .back-name {
    position: absolute; left: 468px; top: 150px;
    color: var(--blue); font-weight: 700; font-size: 26px; letter-spacing: 1px;
  }

  .brand-name {
    position: absolute; left: 60px; top: 165px;
    color: var(--blue); font-weight: 700; font-size: 40px; letter-spacing: 2px;
  }
  .divider {
    position: absolute; left: 330px; top: 70px; width: 1px; height: 230px;
    background: var(--blue-line);
  }
  .details { position: absolute; left: 352px; top: 78px; color: var(--text); }
  .person-name {
    color: var(--blue); font-weight: 700; font-size: 19px; text-transform: uppercase; line-height: 1.1;
  }
  .person-role { font-size: 15px; margin: 4px 0 22px 12px; }
  .contact-list { list-style: none; margin-left: 26px; }
  .contact-list li {
    display: flex; align-items: flex-start; gap: 8px;
    font-size: 14px; line-height: 1.35; margin-bottom: 6px;
  }
  .contact-list svg { flex: none; width: 15px; height: 15px; margin-top: 2px; fill: var(--blue); }
</style>
</head>
<body>
<main class="stage">

  <section class="card card-back">
    <div class="back-pattern" role="img" aria-label="Repeating pattern of faint dark brand marks"></div>
    <div class="back-name">QUENDIX</div>
  </section>

  <section class="card card-front">
    <div class="brand-name">QUENDIX</div>
    <div class="divider"></div>
    <div class="details">
      <div class="person-name">Brent Malvoy</div>
      <div class="person-role">General Manager</div>
      <ul class="contact-list">
        <li>
          <svg viewBox="0 0 24 24"><path d="M6.6 10.8a15.1 15.1 0 0 0 6.6 6.6l2.2-2.2c.3-.3.7-.4 1-.2 1.1.4 2.3.6 3.6.6.6 0 1 .4 1 1V20c0 .6-.4 1-1 1A17 17 0 0 1 3 4c0-.6.4-1 1-1h3.5c.6 0 1 .4 1 1 0 1.3.2 2.5.6 3.6.1.3 0 .7-.2 1z"/></svg>
          <span>0471 592 304</span>
        </li>
        <li>
          <svg viewBox="0 0 24 24"><path d="M12 2a10 10 0 1 0 0 20 10 10 0 0 0 0-20zm6.9 6h-3a15.6 15.6 0 0 0-1.3-3.6A8 8 0 0 1 18.9 8zM12 4c.8 1.2 1.5 2.5 1.9 4h-3.8c.4-1.5 1.1-2.8 1.9-4zM4.3 14a8.2 8.2 0 0 1 0-4h3.4a16 16 0 0 0 0 4zm.8 2h3a15.6 15.6 0 0 0 1.3 3.6A8 8 0 0 1 5.1 16zm3-8h-3a8 8 0 0 1 4.3-3.6C8.8 5.5 8.4 6.7 8.1 8zM12 20c-.8-1.2-1.5-2.5-1.9-4h3.8c-.4 1.5-1.1 2.8-1.9 4zm2.3-6H9.7a14.7 14.7 0 0 1 0-4h4.6a14.7 14.7 0 0 1 0 4zm.3 5.6c.6-1.1 1-2.3 1.3-3.6h3a8 8 0 0 1-4.3 3.6zm1.7-5.6a16 16 0 0 0 0-4h3.4a8.2 8.2 0 0 1 0 4z"/></svg>
          <span>www.quendix.com.au</span>
        </li>
        <li>
          <svg viewBox="0 0 24 24"><path d="M20 4H4a2 2 0 0 0-2 2v12a2 2 0 0 0 2 2h16a2 2 0 0 0 2-2V6a2 2 0 0 0-2-2zm0 4-8 5-8-5V6l8 5 8-5z"/></svg>
          <span>Brent.malvoy@quendix.com.au</span>
        </li>
        <li>
          <svg viewBox="0 0 24 24"><path d="M12 2a7 7 0 0 0-7 7c0 5.2 7 13 7 13s7-7.8 7-13a7 7 0 0 0-7-7zm0 9.5a2.5 2.5 0 1 1 0-5 2.5 2.5 0 0 1 0 5z"/></svg>
          <span>87 Harrowgate Ave<br>Pindarra, QLD, 4000</span>
        </li>
      </ul>
    </div>
  </section>

</main>
</body>
</html>
```